Design a PowerPoint template for a consultancy organisation

I am after a Powerpoint template including three pages a title slide (that should have a title and subtitle), A title and content slide and a section header slide. I expect the company name and/or logo to be prominent and the colors to work well with the logo colors. I have included a copy of the logo

```html
<!DOCTYPE html>
<html lang="en">
<head>
<meta charset="utf-8">
<title>Parley Point – Presentation Template</title>
<link rel="stylesheet" href="https://fonts.googleapis.com/css2?family=Quicksand:wght@400;500;700&display=swap">
<style>
  :root {
    --purple: #6a0dad;
    --green: #8dc63f;
    --slate: #4d4e5e;
    --slate-deep: #363746;
    --ink: #2f3040;
    --paper: #f4f4f5;
    --white: #ffffff;
    --grid: #e2e2e6;
    --muted: #6b6c78;
  }
  * { margin: 0; padding: 0; box-sizing: border-box; }
  html, body { width: 686px; height: 1200px; overflow: hidden; background: var(--white); }
  body { position: relative; font-family: "Quicksand", sans-serif; }
  .slide {
    position: absolute;
    left: 177px;
    width: 331px;
    height: 186px;
    display: block;
    box-shadow: 0 1px 3px rgba(0,0,0,0.18);
  }
  .slide--title-dark   { top: 7px; }
  .slide--title-light  { top: 207px; }
  .slide--title-right  { top: 407px; }
  .slide--divider-dark { top: 607px; }
  .slide--divider-light{ top: 807px; }
  .slide--content      { top: 1007px; }
  .brand { font-family: "Quicksand", sans-serif; font-weight: 700; }
  .headline { font-family: "Quicksand", sans-serif; font-weight: 700; }
  .subline { font-family: "Quicksand", sans-serif; font-weight: 500; fill: var(--green); }
  .on-dark { fill: var(--white); }
  .on-light { fill: var(--purple); }
  .axis-label { font-family: "Quicksand", sans-serif; font-size: 8px; fill: var(--muted); }
  .chart-title { font-family: "Quicksand", sans-serif; font-size: 13px; fill: var(--muted); }
  .footer-note { font-family: "Quicksand", sans-serif; font-size: 5px; fill: var(--ink); }
  .bar--s1 { fill: var(--purple); }
  .bar--s2 { fill: var(--green); }
  .bar--s3 { fill: var(--ink); }
</style>
</head>
<body>
<svg width="0" height="0" style="position:absolute" aria-hidden="true">
  <defs>
    <linearGradient id="duoPhoto" x1="0" y1="0" x2="1" y2="0">
      <stop offset="0" stop-color="#b2d67e"/>
      <stop offset="0.5" stop-color="#8fb860"/>
      <stop offset="0.52" stop-color="#9a5fc8"/>
      <stop offset="1" stop-color="#8a3fc0"/>
    </linearGradient>
    <linearGradient id="darkRoom" x1="0" y1="0" x2="1" y2="1">
      <stop offset="0" stop-color="#55566a"/>
      <stop offset="1" stop-color="#44455a"/>
    </linearGradient>
    <linearGradient id="darkRoomDeep" x1="0" y1="0" x2="1" y2="1">
      <stop offset="0" stop-color="#3e3f50"/>
      <stop offset="1" stop-color="#2e2f3e"/>
    </linearGradient>
    <linearGradient id="lightRoom" x1="0" y1="0" x2="1" y2="1">
      <stop offset="0" stop-color="#f7f7f8"/>
      <stop offset="1" stop-color="#ececef"/>
    </linearGradient>
  </defs>
</svg>

<!-- Title slide, dark -->
<svg class="slide slide--title-dark" viewBox="0 0 703 395" aria-label="Title slide, dark">
  <rect width="703" height="395" fill="url(#darkRoom)" role="img" aria-label="Muted photo of colleagues chatting in an office"/>
  <rect x="350" y="113" width="353" height="207" fill="url(#duoPhoto)" role="img" aria-label="Green and purple tinted photo of colleagues talking over coffee"/>
  <text class="brand on-dark" x="39" y="92" font-size="17">Parley Point</text>
  <text class="headline on-dark" x="34" y="182" font-size="33">Presentation</text>
  <text class="headline on-dark" x="34" y="223" font-size="33">Title Goes Here</text>
  <text class="subline" x="34" y="250" font-size="14">Subtitle Goes Here</text>
</svg>

<!-- Title slide, light -->
<svg class="slide slide--title-light" viewBox="0 0 703 395" aria-label="Title slide, light">
  <rect width="703" height="395" fill="url(#lightRoom)" role="img" aria-label="Faded photo of a team in a bright office"/>
  <rect x="352" y="0" width="351" height="250" fill="url(#duoPhoto)" role="img" aria-label="Green and purple tinted photo of smiling colleagues"/>
  <text class="brand on-light" x="37" y="197" font-size="22">Parley Point</text>
  <text class="headline on-light" x="34" y="314" font-size="33">Presentation Title Goes Here</text>
  <text class="subline" x="34" y="357" font-size="14">Subtitle Goes Here</text>
</svg>

<!-- Title slide, right aligned -->
<svg class="slide slide--title-right" viewBox="0 0 703 395" aria-label="Title slide, right aligned">
  <rect width="703" height="395" fill="url(#darkRoom)" role="img" aria-label="Muted photo of a desk with documents"/>
  <rect x="0" y="0" width="374" height="250" fill="url(#duoPhoto)" role="img" aria-label="Green and purple tinted photo of two silhouettes in a corridor"/>
  <text class="brand on-dark" x="667" y="198" font-size="22" text-anchor="end">Parley Point</text>
  <text class="headline on-dark" x="662" y="314" font-size="33" text-anchor="end">Presentation Title Goes Here</text>
  <text class="subline" x="662" y="357" font-size="14" text-anchor="end">Subtitle Goes Here</text>
</svg>

<!-- Section header, dark -->
<svg class="slide slide--divider-dark" viewBox="0 0 703 395" aria-label="Section header, dark">
  <rect width="703" height="395" fill="url(#darkRoomDeep)" role="img" aria-label="Dark photo of a meeting room"/>
  <rect x="189" y="48" width="325" height="187" fill="url(#duoPhoto)" role="img" aria-label="Green and purple tinted photo of a team meeting"/>
  <text class="headline on-dark" x="351" y="309" font-size="33" text-anchor="middle">Divider Goes Here</text>
  <text class="subline" x="351" y="339" font-size="14" text-anchor="middle">Subtitle Goes Here</text>
</svg>

<!-- Section header, light -->
<svg class="slide slide--divider-light" viewBox="0 0 703 395" aria-label="Section header, light">
  <rect width="703" height="395" fill="url(#lightRoom)" role="img" aria-label="Faded photo of people by an office window"/>
  <rect x="189" y="48" width="325" height="187" fill="url(#duoPhoto)" role="img" aria-label="Green and purple tinted photo of two people talking"/>
  <text class="headline on-light" x="351" y="309" font-size="33" text-anchor="middle">Divider Goes Here</text>
  <text class="subline" x="351" y="339" font-size="14" text-anchor="middle">Subtitle Goes Here</text>
</svg>

<!-- Title and content slide -->
<svg class="slide slide--content" viewBox="0 0 703 395" aria-label="Title and content slide">
  <rect width="703" height="395" fill="var(--white)"/>
  <text class="headline" x="35" y="48" font-size="23" fill="var(--ink)">Chart Example</text>
  <circle cx="38" cy="64" r="3" fill="var(--purple)"/>
  <circle cx="45" cy="64" r="3" fill="var(--purple)"/>
  <circle cx="52" cy="64" r="3" fill="var(--green)"/>
  <text class="brand on-light" x="668" y="62" font-size="15" text-anchor="end">Parley Point</text>

  <g class="chart">
    <text class="chart-title" x="351" y="122" text-anchor="middle">Chart Title</text>
    <g stroke="var(--grid)" stroke-width="1">
      <line x1="55" y1="135" x2="660" y2="135"/>
      <line x1="55" y1="160" x2="660" y2="160"/>
      <line x1="55" y1="186" x2="660" y2="186"/>
      <line x1="55" y1="211" x2="660" y2="211"/>
      <line x1="55" y1="236" x2="660" y2="236"/>
      <line x1="55" y1="262" x2="660" y2="262"/>
      <line x1="55" y1="287" x2="660" y2="287" stroke="#c9c9cf"/>
    </g>
    <g class="axis-label" text-anchor="middle">
      <text x="43" y="138">6</text><text x="43" y="163">5</text><text x="43" y="189">4</text>
      <text x="43" y="214">3</text><text x="43" y="239">2</text><text x="43" y="265">1</text>
      <text x="43" y="290">0</text>
    </g>
    <rect class="bar--s1" x="83" y="178" width="27" height="109"/>
    <rect class="bar--s2" x="117" y="226" width="27" height="61"/>
    <rect class="bar--s3" x="151" y="236" width="27" height="51"/>
    <rect class="bar--s1" x="234" y="224" width="27" height="63"/>
    <rect class="bar--s2" x="268" y="176" width="27" height="111"/>
    <rect class="bar--s3" x="302" y="236" width="27" height="51"/>
    <rect class="bar--s1" x="385" y="198" width="27" height="89"/>
    <rect class="bar--s2" x="419" y="241" width="27" height="46"/>
    <rect class="bar--s3" x="453" y="211" width="27" height="76"/>
    <rect class="bar--s1" x="536" y="173" width="27" height="114"/>
    <rect class="bar--s2" x="570" y="216" width="27" height="71"/>
    <rect class="bar--s3" x="604" y="160" width="27" height="127"/>
    <g class="axis-label" text-anchor="middle">
      <text x="130" y="301">Category 1</text>
      <text x="281" y="301">Category 2</text>
      <text x="432" y="301">Category 3</text>
      <text x="584" y="301">Category 4</text>
    </g>
    <g class="axis-label">
      <rect class="bar--s1" x="283" y="313" width="5" height="5"/><text x="291" y="318">Series 1</text>
      <rect class="bar--s2" x="331" y="313" width="5" height="5"/><text x="339" y="318">Series 2</text>
      <rect class="bar--s3" x="382" y="313" width="5" height="5"/><text x="390" y="318">Series 3</text>
    </g>
  </g>

  <text class="footer-note" x="35" y="372">© Copyright 2021 Parley Point. All rights reserved.</text>
  <rect x="655" y="365" width="12" height="12" rx="1" fill="var(--purple)"/>
</svg>
</body>
</html>
```